Need business cards for our e-assessment business

We need professional looking business cards for our e-assessment business based in Europe. Our company is called Velnor.

You can just use sample name and addresses.

The colours we use are:

#70abe4 (blue)
#FF6600 (orange)

The back side should say: E-assessment made easy

This is the print-shop we are using. Please look at the link for info about formats: http://nl.printqet.com/help/faq/using-my-own-artwork.html

Target Market(s)

Target market is education and large corporations

Industry/Entity Type

Business

```html
<!DOCTYPE html>
<html lang="en">
<head>
<meta charset="utf-8">
<title>Velnor business cards</title>
<link href="https://fonts.googleapis.com/css2?family=Questrial&display=swap" rel="stylesheet">
<style>
  :root {
    --brand-orange: #f26a21;
    --ink-dark: #3a3a3c;
    --ink-grey: #4a4a4a;
    --paper: #ffffff;
    --backdrop: #e9e9ea;
    --card-w: 480px;
    --card-h: 310px;
  }
  * { box-sizing: border-box; margin: 0; padding: 0; }
  html, body {
    width: 1200px;
    height: 800px;
    overflow: hidden;
    background: var(--backdrop);
    font-family: "Questrial", "Century Gothic", sans-serif;
  }
  .card-sheet {
    position: relative;
    width: 1200px;
    height: 800px;
    display: flex;
    justify-content: center;
    align-items: center;
    gap: 60px;
  }
  .card {
    position: relative;
    width: var(--card-w);
    height: var(--card-h);
    overflow: hidden;
  }

  /* Back of the card */
  .card--back { background: var(--brand-orange); }
  .card--back .corner-disc {
    position: absolute;
    left: -125px;
    top: -137px;
    width: 280px;
    height: 280px;
    border-radius: 50%;
    background: var(--paper);
  }
  .card--back .tagline {
    position: absolute;
    right: 32px;
    bottom: 38px;
    color: var(--paper);
    font-size: 46px;
    line-height: 1.1;
    text-align: right;
    letter-spacing: -0.5px;
  }

  /* Front of the card */
  .card--front {
    background: var(--paper);
    text-align: center;
  }
  .brand {
    display: flex;
    align-items: center;
    justify-content: center;
    gap: 26px;
    margin-top: 36px;
  }
  .brand__disc {
    width: 84px;
    height: 84px;
    border-radius: 50%;
    background: var(--brand-orange);
  }
  .brand__name {
    color: var(--ink-dark);
    font-size: 64px;
    line-height: 1;
    letter-spacing: -1px;
  }
  .contact {
    margin-top: 22px;
  }
  .contact__name {
    color: var(--brand-orange);
    font-size: 31px;
    line-height: 1.05;
  }
  .contact__role {
    color: var(--ink-grey);
    font-size: 14px;
    margin-bottom: 12px;
  }
  .contact__line {
    color: var(--ink-grey);
    font-size: 14px;
    line-height: 1.45;
  }
  .contact__label { color: var(--brand-orange); }
</style>
</head>
<body>
  <main class="card-sheet">
    <section class="card card--back" aria-label="Card back">
      <div class="corner-disc"></div>
      <p class="tagline">E-assessment<br>made easy</p>
    </section>

    <section class="card card--front" aria-label="Card front">
      <div class="brand">
        <span class="brand__disc"></span>
        <span class="brand__name">Velnor</span>
      </div>
      <div class="contact">
        <p class="contact__name">Tom Avery</p>
        <p class="contact__role">Regional Manager</p>
        <p class="contact__line"><span class="contact__label">Telephone:</span> +44 1632 960 418</p>
        <p class="contact__line"><span class="contact__label">Email:</span> tom@velnor.com</p>
        <p class="contact__line"><span class="contact__label">Address:</span> Velnor HQ, Harbour Lane,<br>Eastfield, Northam NR4 7LB</p>
      </div>
    </section>
  </main>
</body>
</html>
```